Web Design for an Online Dating Web Site

We need an uncoded web design for a new online dating web site called zMatchy.net. Simplicity and boldness are the key factors in the successful design.
Please look at the requirements document attached for details.
Updates
Dear all,
Please AVOID USING A PICTURE OF A HAPPY COUPLE ON THE HOME PAGE of the site. We highly want to move away from this space as it makes our web site just like another dating web site.
We like something simple with web 2.0 look and feel. The examples in the Requirements Document are exactly the design we are after.
Regards
Tarn
Industry/Entity Type
Dating
Look and feel
Each slider illustrates characteristics of the customer's brand and the style your logo design should communicate.

```html
<!DOCTYPE html>
<html lang="en">
<head>
<meta charset="utf-8">
<title>zMatchy.net – Profile</title>
<link rel="stylesheet" href="https://fonts.googleapis.com/css2?family=Ubuntu:wght@400;500;700&family=Arimo:wght@400;700&display=swap">
<style>
  :root {
    --pink: #e5127d;
    --pink-soft: #e8559c;
    --ink: #1e1e1e;
    --body-bg: #3a3a3a;
    --footer-bg: #2b2b2b;
    --header-top: #5a5a5a;
    --header-light: #f2f2f2;
    --header-dark: #b9b9b9;
    --field: #8d8d8d;
    --field-light: #9a9a9a;
    --topic: #2c2c2c;
    --green: #6fb83a;
    --white: #ffffff;
    --text-light: #e6e6e6;
  }
  * { box-sizing: border-box; margin: 0; padding: 0; }
  html, body { width: 784px; height: 1200px; overflow: hidden; }
  body { position: relative; background: var(--body-bg); font-family: "Arimo", Arial, sans-serif; color: var(--text-light); }
  .abs { position: absolute; }

  /* header */
  .site-header { left: 0; top: 0; width: 784px; height: 104px;
    background: linear-gradient(var(--header-top) 0 11px, var(--header-light) 11px, var(--header-dark) 100%); }
  .brand { left: 64px; top: 28px; display: flex; flex-direction: column; }
  .brand-name { font-family: "Ubuntu", sans-serif; font-size: 44px; font-weight: 500; color: var(--pink); line-height: 46px; letter-spacing: -1px; }
  .brand-url { font-family: "Ubuntu", sans-serif; font-size: 10px; color: #8a8a8a; margin-left: 96px; }
  .main-nav { left: 328px; top: 70px; display: flex; gap: 3px; }
  .main-nav a { font-size: 10px; color: #222; text-decoration: none; background: linear-gradient(#f4f4f4, #bdbdbd);
    border: 1px solid #777; border-radius: 5px; padding: 2px 5px; line-height: 11px; }
  .main-nav a.is-current { font-style: italic; }
  .header-tab { left: 11px; top: 104px; }

  /* video */
  .video-frame { left: 64px; top: 185px; width: 465px; height: 278px; background: var(--white);
    border-radius: 6px; box-shadow: 0 0 22px 8px rgba(255,255,255,.45); overflow: hidden; }
  .video-still { position: absolute; left: 98px; top: 33px; width: 249px; height: 245px;
    background: linear-gradient(#6b6b6b, #151515); }
  .play-button { position: absolute; left: 151px; top: 110px; width: 142px; height: 69px;
    background: rgba(229,18,125,.62); border-radius: 4px; display: flex; align-items: center; justify-content: center; }

  /* topics */
  .topics { left: 601px; top: 188px; list-style: none; }
  .topics li { width: 95px; height: 16px; margin-bottom: 6px; background: var(--topic); border-radius: 4px;
    font-family: "Ubuntu", sans-serif; font-size: 12px; color: var(--white); padding-left: 9px; line-height: 16px; }
  .topics li.is-active { background: var(--pink); }

  /* actions */
  .message-box { left: 64px; top: 504px; width: 172px; height: 52px; background: var(--field);
    border: 1px solid #aaa; border-radius: 4px; }
  .woo-button { left: 275px; top: 503px; width: 84px; height: 28px; background: var(--pink);
    border: 2px solid #f1a3c8; border-radius: 5px; font-family: "Ubuntu", sans-serif; font-size: 12px;
    color: var(--white); text-align: center; line-height: 24px; }
  .woo-badge { left: 331px; top: 490px; width: 22px; height: 22px; border-radius: 50%; background: var(--pink-soft); }
  .pill { top: 540px; width: 40px; height: 12px; border-radius: 4px; font-size: 6px; text-align: center;
    line-height: 12px; color: var(--white); }
  .pill-next { left: 275px; background: var(--green); }
  .pill-friends { left: 319px; background: #8a8a8a; }
  .cursor { left: 280px; top: 548px; }
  .cursor-topics { left: 662px; top: 191px; }

  /* comments */
  .comments-title { left: 64px; top: 584px; font-family: "Ubuntu", sans-serif; font-size: 13px; color: var(--pink); }
  .comment { left: 64px; display: flex; gap: 12px; width: 300px; }
  .avatar { width: 33px; height: 34px; background: linear-gradient(#cfcfcf, #7b7b7b); border: 2px solid #9a9a9a; flex: none; }
  .comment-date { font-size: 7px; color: var(--white); margin-bottom: 4px; }
  .comment-text { font-size: 7px; line-height: 9px; color: var(--text-light); }

  /* footer */
  .site-footer { left: 0; top: 837px; width: 784px; height: 363px; background: var(--footer-bg); overflow: hidden; }
  .footer-glow { position: absolute; left: 300px; top: 150px; width: 420px; height: 420px; border-radius: 50%;
    background: rgba(255,255,255,.05); }
  .footer-tab { left: 29px; top: 836px; }
  .col-title { font-family: "Ubuntu", sans-serif; font-size: 15px; color: var(--pink); }
  .footer-links { list-style: none; margin-top: 9px; }
  .footer-links li { font-size: 7px; line-height: 9px; color: var(--white); }
  .social-icons { display: grid; grid-template-columns: repeat(3, 14px); gap: 12px 20px; margin-top: 12px; }
  .social-icons span { width: 14px; height: 14px; background: #8b8b8b; border-radius: 3px; }
  .social-icons span.round { border-radius: 50%; }
  .counter { position: absolute; width: 31px; }
  .counter b { display: block; height: 17px; background: var(--white); border: 1px solid #999; border-radius: 2px;
    font-size: 10px; color: #333; text-align: center; line-height: 15px; font-weight: 700; }
  .counter i { display: block; height: 8px; margin-top: 2px; border-radius: 2px; background: #5a79b5; }
  .field { position: absolute; background: var(--field-light); border: 1px solid #bbb; border-radius: 4px;
    font-size: 6px; color: #333; padding: 6px 0 0 9px; }
  .send-button { position: absolute; left: 0; top: 248px; width: 87px; height: 22px; background: var(--ink);
    border: 1px solid #ddd; border-radius: 5px; font-size: 7px; color: var(--pink); text-align: center; line-height: 20px; }
  .footer-brand { left: 0; top: 1136px; width: 784px; text-align: center; }
  .footer-brand .brand-name { color: var(--ink); font-size: 40px; }
  .footer-brand .brand-url { margin-left: 90px; color: #777; }
</style>
</head>
<body>
  <header class="abs site-header">
    <div class="abs brand">
      <span class="brand-name">zMatchy</span>
      <span class="brand-url">zmatchy.net</span>
    </div>
    <nav class="abs main-nav">
      <a href="#">My Stuff</a><a href="#" class="is-current">My Messages</a><a href="#">Start Dating</a><a href="#">Sign Out</a><a href="#">Help</a>
    </nav>
  </header>
  <svg class="abs header-tab" width="106" height="53" viewBox="0 0 106 53"><path d="M0 0H106L64 18 53 53 42 18Z" fill="#e5127d"/></svg>

  <section class="abs video-frame">
    <div class="video-still" role="img" aria-label="Profile video still of the member"></div>
    <div class="play-button"><svg width="44" height="36" viewBox="0 0 44 36"><path d="M4 2 42 18 4 34Z" fill="#7a1746" opacity=".8"/></svg></div>
  </section>

  <ul class="abs topics">
    <li class="is-active">Topics</li><li>Topics</li><li>Topics</li><li>Topics</li><li>Topics</li>
  </ul>
  <svg class="abs cursor cursor-topics" width="14" height="16" viewBox="0 0 14 16"><path d="M4 1v8L2 7 1 9l5 6h6l1-6-6-2V1Z" fill="#fff" stroke="#333" stroke-width=".8"/></svg>

  <div class="abs message-box"></div>
  <div class="abs woo-badge"></div>
  <div class="abs woo-button">Woo me</div>
  <div class="abs pill pill-next">Next</div>
  <div class="abs pill pill-friends">Be friends</div>
  <svg class="abs cursor" width="14" height="16" viewBox="0 0 14 16"><path d="M4 1v8L2 7 1 9l5 6h6l1-6-6-2V1Z" fill="#fff" stroke="#333" stroke-width=".8"/></svg>

  <h2 class="abs comments-title">Comments</h2>
  <article class="abs comment" style="top:607px">
    <div class="avatar" role="img" aria-label="Member avatar"></div>
    <div><p class="comment-date">JUL 27, 2011</p>
      <p class="comment-text">Lovely video and a warm smile in your voice. Would you like to meet for coffee this weekend? I know a quiet place near the park ...</p></div>
  </article>
  <article class="abs comment" style="top:668px">
    <div class="avatar" role="img" aria-label="Member avatar"></div>
    <div><p class="comment-date">JUL 27, 2011</p>
      <p class="comment-text">Great topics and a fun style. I enjoy hiking, old films and cooking for friends. Tell me more about your favourite trips so far ...</p></div>
  </article>

  <footer class="abs site-footer">
    <div class="footer-glow"></div>
    <div class="abs" style="left:64px;top:57px">
      <h3 class="col-title">Read More</h3>
      <ul class="footer-links"><li>Why zMatchy</li><li>How it works</li><li>Sign Up</li><li>Login</li><li>About Us</li></ul>
    </div>
    <div class="abs" style="left:209px;top:57px">
      <h3 class="col-title">Find us on</h3>
      <div class="social-icons"><span></span><span class="round"></span><span class="round"></span><span class="round"></span></div>
    </div>
    <div class="abs" style="left:373px;top:57px;width:120px;height:120px">
      <h3 class="col-title">Do u Like us</h3>
      <div class="counter" style="left:0;top:24px"><b>220</b><i></i></div>
      <div class="counter" style="left:45px;top:24px"><b style="color:#3a8fb7">6,314</b><i style="background:#8fc6e0"></i></div>
      <div class="counter" style="left:0;top:64px;width:28px"><b>1</b><i style="background:#cfe0c4"></i></div>
    </div>
    <div class="abs" style="left:536px;top:55px;width:200px;height:280px">
      <h3 class="col-title">Let's Talk</h3>
      <div class="field" style="left:0;top:29px;width:127px;height:20px">Name</div>
      <div class="field" style="left:0;top:57px;width:127px;height:20px">E-mail</div>
      <div class="field" style="left:0;top:85px;width:187px;height:92px">Comments</div>
      <div class="send-button" style="top:193px">Send</div>
    </div>
  </footer>
  <svg class="abs footer-tab" width="70" height="37" viewBox="0 0 70 37"><path d="M0 0H70L40 12 35 37 30 12Z" fill="#fff"/></svg>

  <div class="abs footer-brand">
    <div class="brand-name">zMatchy</div>
    <div class="brand-url">zmatchy.net</div>
  </div>
</body>
</html>
```